New E-Learning Website Design Wanted!

I am creating an E-learning website for those interested in getting certifications in the IT industry.
For example, courses related to VKT, Lomen, RJV certifications and national certifications in the IT industry in Japan will be offered.
You can think of sites such as Pindolia, Kestova, BrickSage, Minotell.
But I am targeting industries in Japan at the moment.
Also, I have uploaded screenshots of pages that I think are good.

The company is Velmont Data
I recently got my company logo designed so I attached pdf file to this project brief.
I would appreciate it if you can make the site match the color scheme of the logo.

Target Market(s)

I am targeting individuals as well as large IT companies in Japan

Industry/Entity Type

Education

Coding

Coded - Design and coding required

Number of Pages Required

4 page

Font styles to use
Sans Serif

Colors

Designer to choose colors to be used in the design.

Requirements
Must have
• One top page design
• One course page (https://tivokhub.example/courses/vkt-hosting-services)
• One learning page(where the learner can see the video)
• One blog page(https://info.tivokhub.example/resources?_ga=2.51827364.27461930.1629384756-830152947.1629384756)
Nice to have
• Pricing page

```html
<!DOCTYPE html>
<html lang="en">
<head>
<meta charset="utf-8">
<title>Velmont Data — Learn to Cloud</title>
<link rel="stylesheet" href="https://fonts.googleapis.com/css2?family=Poppins:wght@400;500;600;700&display=swap">
<style>
:root{
  --navy:#1b2461;
  --ink:#1f2a5c;
  --teal:#27ad9d;
  --teal-blob:#d9f0ed;
  --grey:#8a8fa3;
  --line:#eef1f4;
  --white:#ffffff;
  --vkt:#ff9900;
  --lomen:#2a72c4;
  --rjv:#6a6c70;
}
*{box-sizing:border-box;margin:0;padding:0}
html,body{width:1200px;height:3976px;overflow:hidden}
body{position:relative;font-family:'Poppins',sans-serif;color:var(--ink);background:var(--white)}
.abs{position:absolute}
.btn{position:absolute;display:flex;align-items:center;justify-content:center;background:var(--teal);color:#fff;border-radius:20px;font-size:10px;font-weight:600;text-decoration:none;white-space:nowrap}
.tick{width:12px;height:12px;flex:none}

/* hero */
.hero{position:absolute;left:0;top:0;width:1200px;height:560px;background:radial-gradient(ellipse at 85% 20%,#3a2fb8 0%,#1d1a7a 25%,#0a0a2a 55%,#000 75%)}
.hero-streaks{position:absolute;right:0;top:0;width:760px;height:560px;background:linear-gradient(115deg,transparent 25%,rgba(70,60,220,.35) 45%,rgba(40,90,230,.45) 60%,rgba(25,20,120,.4) 80%,transparent)}
.logo{position:absolute;left:100px;top:18px;display:flex;flex-direction:column;align-items:center;color:#fff;font-size:15px;font-weight:500;letter-spacing:.5px}
.logo .mark{width:34px;height:34px;border-radius:50%;border:2px solid #fff;margin-bottom:4px}
.nav{position:absolute;top:39px;left:450px}
.nav a{color:#fff;font-size:10px;text-decoration:none;font-weight:500;position:absolute;white-space:nowrap}
.login{position:absolute;left:938px;top:32px;width:74px;height:29px;border:1.5px solid #fff;border-radius:16px;color:#fff;font-size:10px;display:flex;align-items:center;justify-content:center}
.hero .signup{left:1025px;top:32px;width:75px;height:29px}
.hero h1{position:absolute;left:225px;top:205px;font-size:31px;line-height:36px;font-weight:600;color:#fff;width:440px}
.hero p{position:absolute;left:225px;top:323px;font-size:11.5px;line-height:18px;color:#fff;width:330px}
.hero .hero-cta{left:225px;top:385px;width:125px;height:28px}

/* feature rows */
.blob-bg{position:absolute;background:var(--teal-blob);border-radius:48% 52% 45% 55%/55% 45% 55% 45%}
.photo{position:absolute;border-radius:55% 45% 48% 52%/45% 55% 45% 55%}
.feature h2{position:absolute;font-size:22px;font-weight:600;color:var(--ink)}
.copy{position:absolute;font-size:9px;line-height:15px;color:var(--grey);width:315px}
.list{position:absolute;list-style:none;font-size:9px;color:var(--grey)}
.list li{display:flex;align-items:center;gap:8px;height:19px;white-space:nowrap}

/* library */
.library-title{position:absolute;left:0;width:1200px;top:1796px;text-align:center;font-size:23px;font-weight:600}
.library-sub{position:absolute;left:0;width:1200px;top:1833px;text-align:center;font-size:11px;color:var(--grey)}
.course{position:absolute;top:1875px;width:238px;height:375px;background:#fff;border-radius:4px}
.course-head{height:137px;display:flex;align-items:center;justify-content:center;color:#fff;font-size:20px;font-weight:600;border-radius:4px 4px 0 0}
.course h3{position:absolute;left:18px;top:155px;font-size:15px;font-weight:600}
.course .copy{left:18px;top:178px;width:205px;font-size:8.5px;line-height:15px}
.course .list{left:18px;top:236px;font-size:8.5px}
.course .list li{height:18.5px}
.course .list li.cont{padding-left:20px}
.course .btn{left:18px;top:355px;width:138px;height:28px;font-size:8.5px}

/* pricing */
.pricing-title{position:absolute;left:0;width:1200px;top:2402px;text-align:center;font-size:23px;font-weight:600;color:#fff}
.pricing-sub{position:absolute;left:0;width:1200px;top:2438px;text-align:center;font-size:11px;color:#fff}
.toggle{position:absolute;top:2470px;height:28px;width:74px;border-radius:14px;font-size:9px;display:flex;align-items:center;justify-content:center;color:#fff}
.plan{position:absolute;background:#fff;border-radius:4px;overflow:hidden;text-align:center}
.plan-icon{margin:20px auto 0;display:block}
.plan h3{font-size:16px;font-weight:500;margin-top:4px;line-height:22px}
.plan .rule{width:60px;height:2px;background:var(--teal);margin:6px auto 0}
.plan .desc{font-size:8.5px;color:var(--grey);line-height:14px;width:170px;margin:14px auto 0}
.plan ul{list-style:none;margin:8px 18px 0;text-align:left;font-size:8.5px;color:var(--grey)}
.plan li{display:flex;align-items:center;gap:8px;height:24px;padding-left:4px}
.plan li:nth-child(odd){background:var(--line)}
.price{font-size:44px;font-weight:600;color:var(--teal);margin-top:18px;line-height:48px}
.price sup{font-size:18px;vertical-align:20px}
.plan-bar{position:absolute;left:0;bottom:0;width:100%;height:42px;background:var(--teal);color:#fff;font-size:9.5px;font-weight:600;display:flex;align-items:center;justify-content:center}

/* footer */
.footer{position:absolute;left:0;top:3640px;width:1200px;height:336px;background:var(--navy)}
.fcol{position:absolute;top:3727px;color:#fff;font-size:9px;line-height:22px}
.fcol a{display:block;color:#fff;text-decoration:none}
</style>
</head>
<body>
<svg width="0" height="0" style="position:absolute">
  <defs>
    <symbol id="tick" viewBox="0 0 12 12"><circle cx="6" cy="6" r="5" fill="none" stroke="#27ad9d" stroke-width="1.1"/><path d="M3.6 6.1l1.7 1.7 3.2-3.3" fill="none" stroke="#27ad9d" stroke-width="1.1"/></symbol>
  </defs>
</svg>

<!-- hero -->
<header class="hero">
  <div class="hero-streaks" role="img" aria-label="Abstract blue light streaks rushing toward the viewer"></div>
  <div class="logo"><span class="mark"></span>Velmont Data</div>
  <nav class="nav">
    <a style="left:0">Home</a><a style="left:67px">Courses</a><a style="left:145px">Features</a><a style="left:225px">For Business</a><a style="left:323px">Pricing</a><a style="left:393px">About</a>
  </nav>
  <span class="login">Login</span>
  <span class="btn signup">Sign Up</span>
  <h1>Provide best learning experience to become a Software Architect</h1>
  <p>Learn to cloud with fun courses and labs taught by the industry's experts.</p>
  <span class="btn hero-cta">Start a Free Trial</span>
</header>
<svg class="abs" style="left:0;top:520px" width="1200" height="60" viewBox="0 0 1200 60" preserveAspectRatio="none"><path d="M0 15 C150 45 350 55 600 40 C850 25 1000 0 1200 10 L1200 60 L0 60Z" fill="#fff"/></svg>

<!-- for business -->
<section class="feature">
  <div class="blob-bg" style="left:165px;top:745px;width:435px;height:360px"></div>
  <div class="photo" role="img" aria-label="Photo of three colleagues working together at a laptop" style="left:180px;top:695px;width:400px;height:380px;background:linear-gradient(135deg,#8a7a6c,#c8b3a2 45%,#5d6d87)"></div>
  <h2 style="left:662px;top:786px">For Business Use</h2>
  <p class="copy" style="left:662px;top:828px">Sed ut perspiciatis unde omnis iste natus error sit voluptatem accusantium doloremque laudantium, totam rem aperiam, eaque ipsa quae ab illo inventore veritatis et quasi architecto beatae.</p>
  <ul class="list" style="left:662px;top:886px">
    <li><svg class="tick"><use href="#tick"/></svg>Nemo enim ipsam voluptatem quia voluptas.</li>
    <li><svg class="tick"><use href="#tick"/></svg>Ut enim ad minima veniam, quis nostrum exercitationem.</li>
    <li><svg class="tick"><use href="#tick"/></svg>At vero eos et accusamus et iusto odio.</li>
    <li><svg class="tick"><use href="#tick"/></svg>On the other hand, we denounce with righteous.</li>
    <li><svg class="tick"><use href="#tick"/></svg>In a free hour, when our power of choice.</li>
  </ul>
  <span class="btn" style="left:662px;top:1006px;width:138px;height:28px">Start Learning Today!</span>
</section>

<!-- for individual -->
<section class="feature">
  <div class="blob-bg" style="left:600px;top:1155px;width:435px;height:390px"></div>
  <div class="photo" role="img" aria-label="Photo of a smiling student with glasses typing on a laptop" style="left:615px;top:1185px;width:420px;height:380px;background:linear-gradient(135deg,#6f6a68,#d9d2cc 50%,#a89a90)"></div>
  <h2 style="left:225px;top:1261px">For Individual Use</h2>
  <p class="copy" style="left:225px;top:1303px;width:300px">Sed ut perspiciatis unde omnis iste natus error sit voluptatem accusantium doloremque laudantium, totam rem aperiam, eaque ipsa quae ab illo inventore veritatis et quasi architecto beatae.</p>
  <ul class="list" style="left:225px;top:1361px">
    <li><svg class="tick"><use href="#tick"/></svg>Nemo enim ipsam voluptatem quia voluptas.</li>
    <li><svg class="tick"><use href="#tick"/></svg>Ut enim ad minima veniam, quis nostrum exercitationem.</li>
    <li><svg class="tick"><use href="#tick"/></svg>At vero eos et accusamus et iusto odio.</li>
    <li><svg class="tick"><use href="#tick"/></svg>On the other hand, we denounce with righteous.</li>
    <li><svg class="tick"><use href="#tick"/></svg>In a free hour, when our power of choice.</li>
  </ul>
  <span class="btn" style="left:225px;top:1481px;width:138px;height:28px">Start Learning Today!</span>
</section>

<!-- course library -->
<svg class="abs" style="left:0;top:1660px" width="1200" height="680" viewBox="0 0 1200 680" preserveAspectRatio="none">
  <path d="M0 20 C200 60 450 55 650 40 C850 25 1000 20 1200 45 L1200 680 L0 680Z" fill="#c7e9e5"/>
  <path d="M0 50 C250 80 450 65 650 55 C850 45 1000 35 1200 60 L1200 680 L0 680Z" fill="#e3f4f2"/>
</svg>
<h2 class="library-title">Explore our course library</h2>
<p class="library-sub">Choose from over 100,000 online video courses with new additions published every month</p>

<article class="course" style="left:225px">
  <div class="course-head" style="background:var(--vkt)">VKT</div>
  <h3>VKT Hosting Services</h3>
  <p class="copy">Ut enim ad minima veniam, quis nostrum exercitationem ullam corporis suscipit laboriosam, nisi ut aliquid.</p>
  <ul class="list">
    <li><svg class="tick"><use href="#tick"/></svg>Vel illum qui dolorem eum fugiat.</li>
    <li><svg class="tick"><use href="#tick"/></svg>Quis autem vel eum iure reprehenderit</li>
    <li class="cont">qui in ea voluptate velit</li>
    <li><svg class="tick"><use href="#tick"/></svg>Vel illum qui dolorem eum fugiat.</li>
    <li><svg class="tick"><use href="#tick"/></svg>Lorem ipsum dolor sit amet.</li>
  </ul>
  <span class="btn">Browse VKT Courses</span>
</article>
<article class="course" style="left:481px">
  <div class="course-head" style="background:var(--lomen)">Lomen Cloud</div>
  <h3>Lomen Cloud</h3>
  <p class="copy">Ut enim ad minima veniam, quis nostrum exercitationem ullam corporis suscipit laboriosam, nisi ut aliquid.</p>
  <ul class="list">
    <li><svg class="tick"><use href="#tick"/></svg>Vel illum qui dolorem eum fugiat.</li>
    <li><svg class="tick"><use href="#tick"/></svg>Quis autem vel eum iure reprehenderit</li>
    <li class="cont">qui in ea voluptate velit</li>
    <li><svg class="tick"><use href="#tick"/></svg>Vel illum qui dolorem eum fugiat.</li>
    <li><svg class="tick"><use href="#tick"/></svg>Lorem ipsum dolor sit amet.</li>
  </ul>
  <span class="btn">Browse Lomen Courses</span>
</article>
<article class="course" style="left:737px">
  <div class="course-head" style="background:var(--rjv)">RJV Cloud</div>
  <h3>RJV Cloud</h3>
  <p class="copy">Ut enim ad minima veniam, quis nostrum exercitationem ullam corporis suscipit laboriosam, nisi ut aliquid.</p>
  <ul class="list">
    <li><svg class="tick"><use href="#tick"/></svg>Vel illum qui dolorem eum fugiat.</li>
    <li><svg class="tick"><use href="#tick"/></svg>Quis autem vel eum iure reprehenderit</li>
    <li class="cont">qui in ea voluptate velit</li>
    <li><svg class="tick"><use href="#tick"/></svg>Vel illum qui dolorem eum fugiat.</li>
    <li><svg class="tick"><use href="#tick"/></svg>Lorem ipsum dolor sit amet.</li>
  </ul>
  <span class="btn">Browse RJV Courses</span>
</article>

<!-- pricing -->
<div class="abs" style="left:0;top:2335px;width:1200px;height:700px;background:var(--navy)"></div>
<svg class="abs" style="left:0;top:2990px" width="1200" height="90" viewBox="0 0 1200 90" preserveAspectRatio="none">
  <path d="M0 30 C250 20 500 5 750 10 C950 15 1100 30 1200 45 L1200 90 L0 90Z" fill="#c7e9e5"/>
  <path d="M0 0 L1200 0 L1200 20 C1000 10 800 20 600 30 C400 40 200 45 0 45Z" fill="#1b2461"/>
</svg>
<svg class="abs" style="left:0;top:3035px" width="1200" height="40" viewBox="0 0 1200 40" preserveAspectRatio="none"><path d="M0 0 C300 0 700 -5 1200 10 L1200 40 L0 40Z" fill="#fff"/></svg>
<section class="pricing">
  <h2 class="pricing-title">We Offer three subscription models</h2>
  <p class="pricing-sub">Ut enim ad minim veniam, quis nostrud exercitation.</p>
  <span class="toggle" style="left:525px;background:var(--teal)">Monthly</span>
  <span class="toggle" style="left:601px;border:1.5px solid #fff">Yearly</span>

  <div class="plan" style="left:272px;top:2548px;width:219px;height:361px">
    <svg class="plan-icon" width="36" height="24" viewBox="0 0 36 24"><path d="M10 5 3 12l7 7M26 5l7 7-7 7M21 2 15 22" fill="none" stroke="#27ad9d" stroke-width="2"/></svg>
    <h3>Programming</h3><div class="rule"></div>
    <p class="desc">Duis aute irure dolor reprehenderit in voluptate velit esse.</p>
    <ul>
      <li><svg class="tick"><use href="#tick"/></svg>Lorem ipsum dolor sit</li>
      <li><svg class="tick"><use href="#tick"/></svg>Consectetur adipiscing elit</li>
      <li><svg class="tick"><use href="#tick"/></svg>Sed do eiusmod tempor</li>
      <li><svg class="tick"><use href="#tick"/></svg>Duis aute irure</li>
      <li><svg class="tick"><use href="#tick"/></svg>Excepteur sint occaecat</li>
    </ul>
    <div class="price"><sup>$</sup>27</div>
    <div class="plan-bar">Subscribe Today!</div>
  </div>

  <div class="plan" style="left:709px;top:2548px;width:219px;height:361px">
    <svg class="plan-icon" width="24" height="24" viewBox="0 0 24 24"><path d="M7 11v10H3V11zM7 11l4-8c2 0 3 1 2.5 3L13 10h6c1.5 0 2.3 1.2 2 2.5l-1.6 6.5c-.3 1.2-1.2 2-2.4 2H7" fill="none" stroke="#27ad9d" stroke-width="1.8" stroke-linejoin="round"/></svg>
    <h3>All in One</h3><div class="rule"></div>
    <p class="desc">Duis aute irure dolor reprehenderit in voluptate velit esse.</p>
    <ul>
      <li><svg class="tick"><use href="#tick"/></svg>Lorem ipsum dolor sit</li>
      <li><svg class="tick"><use href="#tick"/></svg>Consectetur adipiscing elit</li>
      <li><svg class="tick"><use href="#tick"/></svg>Sed do eiusmod tempor</li>
      <li><svg class="tick"><use href="#tick"/></svg>Duis aute irure</li>
      <li><svg class="tick"><use href="#tick"/></svg>Excepteur sint occaecat</li>
    </ul>
    <div class="price"><sup>$</sup>87</div>
    <div class="plan-bar">Subscribe Today!</div>
  </div>

  <div class="plan" style="left:491px;top:2529px;width:218px;height:397px;border:3px solid var(--teal);border-top-width:14px;border-radius:6px;z-index:2">
    <svg class="plan-icon" width="36" height="24" viewBox="0 0 36 24"><path d="M10 21h17a6 6 0 0 0 0-12 8 8 0 0 0-15.5-2A7 7 0 0 0 10 21z" fill="none" stroke="#27ad9d" stroke-width="2"/></svg>
    <h3>Cloud</h3><div class="rule"></div>
    <p class="desc">Duis aute irure dolor reprehenderit in voluptate velit esse.</p>
    <ul>
      <li><svg class="tick"><use href="#tick"/></svg>Lorem ipsum dolor sit</li>
      <li><svg class="tick"><use href="#tick"/></svg>Consectetur adipiscing elit</li>
      <li><svg class="tick"><use href="#tick"/></svg>Sed do eiusmod tempor</li>
      <li><svg class="tick"><use href="#tick"/></svg>Duis aute irure</li>
      <li><svg class="tick"><use href="#tick"/></svg>Excepteur sint occaecat</li>
    </ul>
    <div class="price"><sup>$</sup>47</div>
    <div class="plan-bar" style="height:52px;font-size:11px">Subscribe Today!</div>
  </div>
</section>

<!-- certification call to action -->
<section class="feature">
  <div class="blob-bg" style="left:140px;top:3150px;width:435px;height:390px;background:#e6f5f3"></div>
  <div class="photo" role="img" aria-label="Collage of colourful certification course cover artwork" style="left:150px;top:3125px;width:420px;height:380px;background:linear-gradient(150deg,#7b2fa0 0%,#4b2a9a 35%,#f59a1f 60%,#3a3cd0 85%)"></div>
  <h2 style="left:662px;top:3222px;width:330px;line-height:28px">Ready to learn? Training courses for national certification are one time payment courses</h2>
  <p class="copy" style="left:662px;top:3353px">Sed ut perspiciatis unde omnis iste natus error sit voluptatem accusantium doloremque laudantium.</p>
  <span class="btn" style="left:662px;top:3400px;width:138px;height:28px">Start Learning Today!</span>
</section>

<!-- footer -->
<svg class="abs" style="left:0;top:3590px" width="1200" height="60" viewBox="0 0 1200 60" preserveAspectRatio="none">
  <path d="M0 55 C150 30 350 10 600 12 C850 14 1000 30 1200 45 L1200 60 L0 60Z" fill="#8a93b3"/>
  <path d="M0 60 C200 45 400 40 650 40 C900 40 1050 48 1200 56 L1200 60Z" fill="#1b2461"/>
</svg>
<footer class="footer"></footer>
<div class="fcol" style="left:100px">
  <strong style="font-size:11px;font-weight:600">Call. 1-800-555-0142</strong><br>
  <span style="display:block;margin-top:-6px">e. info@velmontdata.example</span>
  <span style="display:block;margin-top:10px;line-height:15px">Velmont Data<br>Lorem Ipsum Sit Amet<br>Dummy Pin</span>
</div>
<div class="fcol" style="left:350px"><a>Subscription Plan</a><a>certification courses</a><a>About</a><a>Blog</a><a>Careers</a><a>Contact</a></div>
<div class="fcol" style="left:600px"><a>Sitemap</a><a>Terms</a><a>Privacy Policy</a><a>Cookie</a></div>
<div class="fcol" style="left:788px;width:188px;text-align:right">
  <strong style="font-size:11px;font-weight:600">Sign up Newsletter</strong>
  <div style="margin-top:6px;height:30px;border:1px solid #fff;display:flex;align-items:center;justify-content:space-between;padding:0 10px;text-align:left">Your Email
    <svg width="12" height="8" viewBox="0 0 12 8"><path d="M0 4h11M8 1l3 3-3 3" fill="none" stroke="#27ad9d" stroke-width="1.2"/></svg></div>
  <div style="margin-top:16px;font-size:8px">Streamo · Chirply · Facelink · Proline</div>
</div>
<div class="abs" style="left:942px;top:3905px;width:34px;height:34px;border-radius:50%;border:2px solid #fff;opacity:.8"></div>
<p class="abs" style="left:100px;top:3924px;font-size:8px;color:#fff">© Velmont Data 2020. All rights reserved.</p>
</body>
</html>
```